New banner design for mortgage broker

Looking for a banner design for mortgage broking company.
- need to use logo
- need to use colours from the logo
- like to use the headshot somehow.
- use slogan ' Helping to navigate your finance journey'
- include listing our services. Home Loans, Investment Loans, First Home Buyers, Self-employed Specialist, Car loans, Past Credit issues.
- call to action to get in contact today on 1300 642 917 or www.harbourfinvo.com.au
- Banner size 2.4m x 0.6m

```html
<!DOCTYPE html>
<html lang="en">
<head>
<meta charset="utf-8">
<title>Harbourfin Lending – Banner</title>
<link rel="stylesheet" href="https://fonts.googleapis.com/css2?family=Montserrat:wght@500;600;700;800&family=Oswald:wght@600;700&family=Mrs+Saint+Delafield&display=swap">
<style>
  :root {
    --brand-purple: #51267f;
    --ink: #1c1c1c;
    --slate: #4f5154;
    --paper: #fbfbfb;
    --white: #ffffff;
    --photo-light: #d9cfc6;
    --photo-dark: #2a2f4a;
  }
  * { margin: 0; padding: 0; box-sizing: border-box; }
  html, body { width: 1200px; height: 317px; overflow: hidden; background: var(--paper); }
  .banner {
    position: relative;
    width: 1200px;
    height: 317px;
    overflow: hidden;
    background: var(--paper);
    font-family: "Montserrat", sans-serif;
  }
  .banner__shapes { position: absolute; inset: 0; }
  .brand-name {
    position: absolute;
    left: 23px; top: 18px;
    color: var(--white);
    font-family: "Montserrat", sans-serif;
    font-weight: 600;
    font-size: 17px;
    letter-spacing: 0.5px;
  }
  .headshot {
    position: absolute;
    left: 40px; top: 75px;
    width: 212px; height: 242px;
    border-radius: 100px 100px 0 0;
    background: linear-gradient(180deg, var(--photo-light) 0%, #c7aa8a 45%, var(--photo-dark) 78%);
  }
  .slogan { position: absolute; left: 0; top: 0; }
  .slogan__script {
    position: absolute;
    font-family: "Mrs Saint Delafield", cursive;
    color: #3a3a3a;
    white-space: nowrap;
    line-height: 1;
  }
  .slogan__helping { left: 283px; top: 52px; font-size: 62px; transform: rotate(-8deg); transform-origin: left center; }
  .slogan__to-your { left: 505px; top: 86px; font-size: 34px; transform: rotate(-8deg); transform-origin: left center; }
  .slogan__journey { left: 336px; top: 238px; font-size: 56px; color: var(--brand-purple); transform: rotate(-8deg); transform-origin: left center; }
  .slogan__bold {
    position: absolute;
    font-family: "Oswald", sans-serif;
    font-weight: 700;
    text-transform: uppercase;
    line-height: 1;
    white-space: nowrap;
    transform: rotate(-8deg);
    transform-origin: left center;
    transform-box: border-box;
  }
  .slogan__navigate { left: 312px; top: 116px; font-size: 50px; color: var(--brand-purple); }
  .slogan__finance { left: 316px; top: 160px; font-size: 80px; color: var(--slate); letter-spacing: -1px; }

  .services { position: absolute; left: 642px; top: 56px; }
  .services__title {
    font-weight: 700;
    font-size: 24px;
    color: var(--ink);
    letter-spacing: 0.3px;
  }
  .services__item {
    position: absolute;
    font-weight: 600;
    font-size: 13.5px;
    color: var(--ink);
    white-space: nowrap;
    padding-left: 18px;
  }
  .services__item::before {
    content: "";
    position: absolute;
    left: 0; top: 50%;
    width: 6px; height: 6px;
    margin-top: -4px;
    border-radius: 50%;
    background: var(--ink);
  }
  .arrow-icon { position: absolute; left: 1058px; top: 118px; }
  .contact {
    position: absolute;
    left: 987px; top: 229px;
    width: 200px;
    text-align: center;
    color: var(--white);
  }
  .contact__phone { font-weight: 800; font-size: 15px; letter-spacing: 0.8px; }
  .contact__web { font-weight: 500; font-size: 7.5px; letter-spacing: 1.4px; margin-top: 1px; }
  .contact__button {
    display: inline-block;
    margin-top: 6px;
    width: 86px; height: 24px;
    line-height: 24px;
    border-radius: 12px;
    background: var(--white);
    color: var(--ink);
    font-weight: 700;
    font-size: 7.5px;
    letter-spacing: 0.3px;
  }
</style>
</head>
<body>
<main class="banner">
  <svg class="banner__shapes" width="1200" height="317" viewBox="0 0 1200 317" aria-hidden="true">
    <path fill="var(--brand-purple)" d="M0 0 H268 C252 58 214 88 162 100 C84 116 22 150 0 200 Z"/>
    <path fill="var(--brand-purple)" d="M1200 118 C1185 170 1140 200 1075 203 C1000 207 945 250 932 317 H1200 Z"/>
  </svg>

  <div class="brand-name">Harbourfin</div>

  <div class="headshot" role="img" aria-label="Headshot photo of the mortgage broker"></div>

  <div class="slogan">
    <span class="slogan__script slogan__helping">Helping</span>
    <span class="slogan__script slogan__to-your">to your</span>
    <span class="slogan__bold slogan__navigate">Navigate</span>
    <span class="slogan__bold slogan__finance">Finance</span>
    <span class="slogan__script slogan__journey">journey</span>
  </div>

  <section class="services">
    <h2 class="services__title">OUR SERVICES</h2>
    <div class="services__item" style="left:2px; top:36px;">Home Loans</div>
    <div class="services__item" style="left:2px; top:79px;">Investment Loans</div>
    <div class="services__item" style="left:2px; top:123px;">First Home Buyers</div>
    <div class="services__item" style="left:2px; top:168px;">Self-employed Specialist</div>
    <div class="services__item" style="left:2px; top:213px;">Car loans</div>
    <div class="services__item" style="left:215px; top:33px;">Past Credit issues</div>
  </section>

  <svg class="arrow-icon" width="34" height="56" viewBox="0 0 34 56" aria-hidden="true">
    <path d="M6 2 L3 10 L16 34 L10 36 L30 52 L28 28 L22 32 Z" fill="none" stroke="#333" stroke-width="1.6" stroke-linejoin="round"/>
  </svg>

  <div class="contact">
    <div class="contact__phone">1300 642 917</div>
    <div class="contact__web">www.harbourfinvo.com.au</div>
    <div class="contact__button">CONTACT US</div>
  </div>
</main>
</body>
</html>
```